Business Card Design

New business card design

Target Market(s)

Residential & Commercial Property Managers

Industry/Entity Type

Plumbing Services

Contact Information for Business Card

Name - Owen Tredgold, title - Director, Phone Number - 0431 862 507, email - owen@rvb-plumbing.com.au, Company ABN - 73 215 904 386,

Font styles to use
Sans Serif

Colors
0054AA
0677BA
7BADD7
CADEEF
E8F1F8

```html
<!DOCTYPE html>
<html lang="en">
<head>
<meta charset="utf-8">
<title>RVB Plumbing – Business Card</title>
<link rel="stylesheet" href="https://fonts.googleapis.com/css2?family=Arimo:wght@400;700&display=swap">
<style>
  :root {
    --backdrop: #ececec;
    --card-dark: #1f242b;
    --card-edge: #19a3e0;
    --accent-blue: #19a3e0;
    --text-light: #f2f4f6;
    --text-muted: #8a929b;
    --band-white: #ffffff;
    --band-text: #3a3f45;
    --emboss: #2c333c;
  }
  * { box-sizing: border-box; margin: 0; padding: 0; }
  html, body { width: 1200px; height: 900px; overflow: hidden; }
  body {
    background: var(--backdrop);
    font-family: "Arimo", Arial, sans-serif;
    position: relative;
  }
  .card {
    position: absolute;
    left: 337px;
    width: 525px;
    height: 300px;
    border-radius: 28px;
    background: var(--card-dark);
    border: 3px solid var(--card-edge);
    overflow: hidden;
  }
  .card--front { top: 100px; }
  .card--back { top: 500px; }

  .brand {
    position: absolute;
    display: flex;
    align-items: center;
    gap: 10px;
    color: var(--text-light);
    font-weight: 400;
    letter-spacing: 1px;
  }
  .card--front .brand { left: 36px; top: 104px; font-size: 30px; }
  .brand__dot {
    width: 14px; height: 14px; border-radius: 50%;
    background: var(--accent-blue);
    flex: none;
  }

  .divider {
    position: absolute;
    left: 262px; top: 56px;
    width: 1px; height: 150px;
    background: var(--text-muted);
  }

  .contact {
    position: absolute;
    left: 282px; top: 74px;
    color: var(--text-light);
  }
  .contact__name {
    color: var(--accent-blue);
    font-weight: 700;
    font-size: 21px;
    text-transform: uppercase;
    letter-spacing: 0.3px;
  }
  .contact__title { font-size: 15px; margin: 4px 0 12px; }
  .contact__line {
    display: flex; align-items: center; gap: 6px;
    font-size: 15px; margin-bottom: 6px;
  }
  .contact__icon { width: 12px; height: 12px; flex: none; }

  .abn-band {
    position: absolute;
    left: 0; bottom: 26px;
    width: 390px; height: 36px;
    background: var(--band-white);
    display: flex; align-items: center;
    padding-left: 160px;
    font-size: 15px;
    color: var(--band-text);
  }
  .abn-band__label { color: var(--accent-blue); margin-right: 5px; }
  .accent-band {
    position: absolute;
    left: 390px; bottom: 26px;
    width: 140px; height: 36px;
    background: var(--accent-blue);
  }
  .accent-band__dot {
    position: absolute;
    left: 372px; bottom: 24px;
    width: 40px; height: 40px; border-radius: 50%;
    background: var(--accent-blue);
    border: 3px solid var(--card-dark);
  }

  .card--back .brand {
    left: 50%; top: 50%;
    transform: translate(-50%, -50%);
    font-size: 56px;
    color: var(--emboss);
    gap: 16px;
  }
  .card--back .brand__dot { width: 20px; height: 20px; }
</style>
</head>
<body>
  <section class="card card--front" aria-label="Business card front">
    <div class="brand"><span class="brand__dot"></span><span>rvb plumbing</span></div>
    <div class="divider"></div>
    <div class="contact">
      <p class="contact__name">Owen Tredgold</p>
      <p class="contact__title">Director</p>
      <p class="contact__line">
        <svg class="contact__icon" viewBox="0 0 12 12" aria-hidden="true"><path d="M2 1h3l1 3-2 1a7 7 0 0 0 3 3l1-2 3 1v3c-6 0-9-3-9-9z" fill="#f2f4f6"/></svg>
        0431 862 507
      </p>
      <p class="contact__line">
        <svg class="contact__icon" viewBox="0 0 12 12" aria-hidden="true"><rect x="1" y="2.5" width="10" height="7" rx="1" fill="#f2f4f6"/><path d="M1.5 3l4.5 3.5L10.5 3" stroke="#1f242b" fill="none"/></svg>
        owen@rvb-plumbing.com.au
      </p>
    </div>
    <div class="abn-band"><span class="abn-band__label">ABN:</span>73 215 904 386</div>
    <div class="accent-band"></div>
    <div class="accent-band__dot"></div>
  </section>

  <section class="card card--back" aria-label="Business card back">
    <div class="brand"><span class="brand__dot"></span><span>rvb plumbing</span></div>
  </section>
</body>
</html>
```